Designing a website for Korvale Pest Solutions PTY LTD

Pest control company looking for someone to build an informative website containing services we offer and an online inquiry form.
Commercial premises - Specialising in - Rodent control, stored product pest control, flying insect control, ant, spider and insect control, Termite inspections and treatments. Termite management systems on a commercial scale.
Facilities we service
Commercial - shopping centres, transport facilities, restaurants, pubs, clubs, bars food manufacturing facilities.
Residential - Houses specialising in - Rodent, Ant, Spider, Cockroach and Termite control. Termite inspections, Pre - purchase inspections, Termite treatments, Termite management systems.
Target Market(s)
Mainly commercial and industrial clients and Residential clients.
Industry/Entity Type
Pest Control
Number of Pages Required
1 page
Look and feel
Each slider illustrates characteristics of the customer's brand and the style your logo design should communicate.

```html
<!DOCTYPE html>
<html lang="en">
<head>
<meta charset="utf-8">
<title>Korvale Pest Solutions PTY LTD</title>
<link rel="stylesheet" href="https://fonts.googleapis.com/css2?family=Exo+2:wght@400;600;800&family=Montserrat:wght@600;700&family=Rajdhani:wght@400;500;700&display=swap">
<style>
:root{
  --green:#2f8110;
  --green-dark:#25680b;
  --black:#0b0b0b;
  --white:#ffffff;
  --text:#5c5c5c;
  --grey-light:#f1f1f1;
}
*{margin:0;padding:0;box-sizing:border-box}
html,body{width:1200px;height:3646px;overflow:hidden;background:var(--white)}
body{position:relative;font-family:"Rajdhani",sans-serif;color:var(--black)}
.abs{position:absolute}
.topline{left:0;top:0;width:1200px;height:4px;background:var(--green)}
.hero-art{left:0;top:0}
.header-bar{left:0;top:4px;width:1200px;height:82px;background:var(--white)}
.logo-blob{left:118px;top:10px;width:264px;height:118px;background:var(--white);border-radius:0 0 132px 132px/0 0 60px 60px}
.brand{font-family:"Exo 2",sans-serif;font-weight:800;color:var(--black);display:flex;align-items:center;gap:10px}
.brand .dot{width:18px;height:18px;border-radius:50%;background:var(--green)}
.brand-header{left:172px;top:30px;font-size:40px}
.nav{top:34px;font-family:"Montserrat",sans-serif;font-weight:700;font-size:14px;color:#222;display:flex}
.nav a{position:absolute;white-space:nowrap;color:#222;text-decoration:none}
.nav .active::after{content:"";position:absolute;left:0;right:0;top:22px;height:3px;background:var(--green);border-radius:2px}
.btn{display:flex;align-items:center;justify-content:center;border-radius:32px;font-family:"Montserrat",sans-serif;font-weight:700;color:var(--white);background:var(--green);font-size:16px;letter-spacing:.3px}
.btn-dark{background:var(--black)}
.login{left:947px;top:21px;width:107px;height:45px;font-size:16px}
.hero-title{left:142px;top:222px;font-family:"Exo 2",sans-serif;font-size:60px;line-height:67px;color:var(--black);white-space:nowrap}
.hero-title b{font-weight:800}
.hero-title .accent{color:var(--green)}
.hero-title span.light{font-weight:400;letter-spacing:1px}
.get-started{left:143px;top:456px;width:182px;height:63px}
.dots{left:1152px;top:334px;display:flex;flex-direction:column;gap:8px}
.dots i{display:block;width:10px;height:10px;border-radius:50%;background:var(--white)}
.dots i.on{background:var(--green)}
.welcome{left:0;width:1200px;top:862px;text-align:center}
.welcome h1{font-family:"Exo 2",sans-serif;font-weight:800;font-size:46px;line-height:56px}
.welcome h2{font-family:"Exo 2",sans-serif;font-weight:400;font-size:38px;line-height:46px;color:var(--green);margin-top:4px}
.welcome p{width:830px;margin:26px auto 0;font-size:16px;line-height:28px;color:var(--text)}
.read-more{left:509px;top:1183px;width:181px;height:62px}
.panel-art{left:0;top:1250px}
.panel-title{font-family:"Exo 2",sans-serif;font-weight:800;font-size:40px;color:var(--white);text-align:center}
.t-commercial{left:100px;width:400px;top:1700px}
.t-residential{left:708px;width:400px;top:1676px}
.b-commercial{left:209px;top:1790px;width:183px;height:62px}
.b-residential{left:818px;top:1766px;width:181px;height:62px}
.spec-title{left:0;width:1200px;top:2042px;text-align:center;font-family:"Exo 2",sans-serif;font-weight:800;font-size:48px}
.spec-title span{color:var(--green);font-weight:400}
.spec{top:2183px;width:240px;text-align:center}
.spec svg{display:block;margin:0 auto}
.spec p{margin-top:18px;font-family:"Montserrat",sans-serif;font-weight:600;font-size:15px;line-height:24px;color:#222}
.view-more{left:509px;top:2492px;width:181px;height:62px}
.touch-art{left:0;top:2620px}
.touch-title{left:0;width:1200px;top:2778px;text-align:center;font-family:"Exo 2",sans-serif;font-weight:800;font-size:48px;color:var(--white)}
.touch-title span{color:var(--green);font-weight:400}
.field{background:var(--white);border:1px solid #ddd;font-family:"Rajdhani",sans-serif;font-size:17px;color:#333;padding:14px 20px}
.submit{left:509px;top:3177px;width:181px;height:62px}
.brand-footer{left:148px;top:3490px;font-size:62px}
.footer-nav{left:492px;top:3456px;font-family:"Montserrat",sans-serif;font-weight:700;font-size:18px;color:var(--black);word-spacing:2px}
.footer-nav span{margin:0 10px;font-weight:600}
.copyright{left:492px;top:3504px;font-size:14px;color:#444}
.social{top:3559px;width:44px;height:44px;border:2px solid var(--green);border-radius:50%}
</style>
</head>
<body>
<div class="abs topline"></div>

<svg class="abs hero-art" width="1200" height="800" viewBox="0 0 1200 800">
  <defs>
    <linearGradient id="heroFill" x1="0" y1="0" x2="1" y2="0">
      <stop offset="0" stop-color="#f3f3f3"/>
      <stop offset="0.35" stop-color="#e6e6e6"/>
      <stop offset="0.55" stop-color="#c9a27e"/>
      <stop offset="0.75" stop-color="#7a7a72"/>
      <stop offset="1" stop-color="#6d4a3c"/>
    </linearGradient>
  </defs>
  <path d="M0,560 Q600,1030 1200,545 L1200,86 L0,86Z" fill="#0b0b0b"/>
  <path d="M0,540 Q600,975 1200,522 L1200,86 L0,86Z" fill="#2f8110"/>
  <path role="img" aria-label="Technician in orange overalls fogging a garden path by a gate" d="M0,532 Q600,935 1200,505 L1200,86 L0,86Z" fill="url(#heroFill)"/>
</svg>

<div class="abs header-bar"></div>
<div class="abs logo-blob"></div>
<div class="abs brand brand-header"><i class="dot"></i>Korvale</div>

<nav class="abs nav" style="left:0;top:34px">
  <a class="active" style="left:465px">HOME</a>
  <a style="left:540px">ABOUT US</a>
  <a style="left:644px">SERVICES</a>
  <a style="left:744px">NEWS</a>
  <a style="left:819px">CONTACT US</a>
</nav>
<div class="abs btn login">LOGIN</div>

<div class="abs hero-title"><b class="accent">KORVALE</b> <b>PEST</b><br><span class="light">SOLUTIONS</span><br><b>PTY LTD</b></div>
<div class="abs btn get-started">GET STARTED</div>
<div class="abs dots"><i></i><i></i><i class="on"></i><i></i><i></i></div>

<section class="abs welcome">
  <h1>WELCOME TO</h1>
  <h2>KORVALE PEST SOLUTIONS PTY LTD</h2>
  <p>Lorem ipsum dolor sit amet, consectetur adipiscing elit, sed do eiusmod tempor incididunt ut labore et dolore magna aliquis ipsum suspendisse ultrices gravidas commodo viverra maecenas accumsan lacus vel facilisrem ipsum dolor sit amet, consectetur adipiscing elit, sed do eiusmod tempor incididunt ut labore et dolore magnaliquis ipsum suspendisse ultrices gravidas commodo viverra maecenas accumsan lacus vum dolor sit amet, consetetur adipiscing sed do eiusmod tempor incididunt ut labore et dolore magna aliquis ipsum suspendisse ultrices gravidas</p>
</section>
<div class="abs btn read-more">READ MORE</div>

<svg class="abs panel-art" width="1200" height="740" viewBox="0 1250 1200 740">
  <defs>
    <linearGradient id="comFill" x1="0" y1="0" x2="1" y2="1">
      <stop offset="0" stop-color="#9a9a9a"/><stop offset="1" stop-color="#3d3d3d"/>
    </linearGradient>
    <linearGradient id="resFill" x1="0" y1="0" x2="0" y2="1">
      <stop offset="0" stop-color="#2f8110"/><stop offset="0.6" stop-color="#1f5c08"/><stop offset="1" stop-color="#2f8110"/>
    </linearGradient>
  </defs>
  <path d="M0,1443 Q300,1206 600,1436 L600,1470 L0,1470Z" fill="#2f8110"/>
  <path role="img" aria-label="Worker in protective suit spraying a commercial kitchen" d="M0,1478 Q300,1240 600,1468 L600,1875 Q300,2050 0,1882Z" fill="url(#comFill)"/>
  <path d="M608,1825 Q900,2010 1200,1800 L1200,1840 Q900,2050 608,1860Z" fill="#0b0b0b"/>
  <path role="img" aria-label="Residential house with palm trees and lawn" d="M608,1358 Q900,1235 1200,1373 L1200,1800 Q900,2015 608,1825Z" fill="url(#resFill)"/>
</svg>
<div class="abs panel-title t-commercial">Commercial</div>
<div class="abs btn b-commercial">READ MORE</div>
<div class="abs panel-title t-residential">Residential</div>
<div class="abs btn btn-dark b-residential">READ MORE</div>

<h2 class="abs spec-title">SPECIALISING <span>IN</span></h2>

<div class="abs spec" style="left:104px">
  <svg width="146" height="150" viewBox="0 0 146 150">
    <path d="M6,73 A67,67 0 0 1 140,73" fill="none" stroke="#0b0b0b" stroke-width="6"/>
    <path d="M6,73 A67,67 0 0 0 140,73" fill="none" stroke="#2f8110" stroke-width="6"/>
    <circle cx="73" cy="73" r="32" fill="none" stroke="#222" stroke-width="3"/>
    <ellipse cx="73" cy="76" rx="16" ry="10" fill="none" stroke="#222" stroke-width="2.5"/>
    <line x1="51" y1="51" x2="95" y2="95" stroke="#222" stroke-width="3"/>
  </svg>
  <p>RODENT CONTROL</p>
</div>
<div class="abs spec" style="left:353px">
  <svg width="146" height="150" viewBox="0 0 146 150">
    <path d="M6,73 A67,67 0 0 1 140,73" fill="none" stroke="#0b0b0b" stroke-width="6"/>
    <path d="M6,73 A67,67 0 0 0 140,73" fill="none" stroke="#2f8110" stroke-width="6"/>
    <circle cx="73" cy="73" r="32" fill="none" stroke="#222" stroke-width="3"/>
    <ellipse cx="73" cy="75" rx="10" ry="16" fill="none" stroke="#222" stroke-width="2.5"/>
    <line x1="51" y1="51" x2="95" y2="95" stroke="#222" stroke-width="3"/>
  </svg>
  <p>STORED PRODUCT<br>PEST CONTROL</p>
</div>
<div class="abs spec" style="left:602px">
  <svg width="146" height="150" viewBox="0 0 146 150">
    <path d="M6,73 A67,67 0 0 1 140,73" fill="none" stroke="#0b0b0b" stroke-width="6"/>
    <path d="M6,73 A67,67 0 0 0 140,73" fill="none" stroke="#2f8110" stroke-width="6"/>
    <rect x="52" y="62" width="22" height="42" rx="3" fill="none" stroke="#222" stroke-width="2.5"/>
    <rect x="57" y="50" width="12" height="12" fill="none" stroke="#222" stroke-width="2.5"/>
    <circle cx="63" cy="86" r="6" fill="none" stroke="#222" stroke-width="2"/>
    <circle cx="86" cy="52" r="2" fill="#222"/><circle cx="95" cy="46" r="2" fill="#222"/><circle cx="98" cy="62" r="2" fill="#222"/>
  </svg>
  <p>FLYING INSECT<br>CONTROL</p>
</div>
<div class="abs spec" style="left:851px">
  <svg width="146" height="150" viewBox="0 0 146 150">
    <path d="M6,73 A67,67 0 0 1 140,73" fill="none" stroke="#0b0b0b" stroke-width="6"/>
    <path d="M6,73 A67,67 0 0 0 140,73" fill="none" stroke="#2f8110" stroke-width="6"/>
    <g fill="none" stroke="#222" stroke-width="2">
      <line x1="73" y1="41" x2="73" y2="105"/><line x1="41" y1="73" x2="105" y2="73"/>
      <line x1="50" y1="50" x2="96" y2="96"/><line x1="96" y1="50" x2="50" y2="96"/>
      <polygon points="73,49 90,56 97,73 90,90 73,97 56,90 49,73 56,56"/>
      <polygon points="73,61 81,65 85,73 81,81 73,85 65,81 61,73 65,65"/>
    </g>
  </svg>
  <p>SPIDER AND INSECT<br>CONTROL</p>
</div>
<div class="abs btn view-more">VIEW MORE</div>

<svg class="abs touch-art" width="1200" height="800" viewBox="0 2620 1200 800">
  <path d="M0,2712 Q350,2580 1200,2730 L1200,3340 Q600,3480 0,3260Z" fill="#2f8110"/>
  <path role="img" aria-label="Darkened photo of a technician treating a house garden" d="M0,2740 Q400,2600 1200,2735 L1200,3310 Q600,3450 0,3265Z" fill="#1e1e1e"/>
</svg>
<h2 class="abs touch-title">GET IN <span>TOUCH</span></h2>
<div class="abs field" style="left:233px;top:2884px;width:360px;height:51px">First Name</div>
<div class="abs field" style="left:605px;top:2884px;width:360px;height:51px">Last Name</div>
<div class="abs field" style="left:233px;top:2948px;width:360px;height:52px">Email address</div>
<div class="abs field" style="left:605px;top:2948px;width:360px;height:52px">Phone Number</div>
<div class="abs field" style="left:233px;top:3013px;width:732px;height:113px">Message</div>
<div class="abs btn submit">SUBMIT</div>

<div class="abs brand brand-footer"><i class="dot"></i>Korvale</div>
<div class="abs footer-nav">HOME<span>/</span>ABOUT US<span>/</span>SERVICES<span>/</span>NEWS<span>/</span>CONTACT US</div>
<div class="abs copyright">© 2021 Korvale Pest Solutions PTY LTD. All rights reserved.Privacy Terms of Use</div>
<div class="abs social" style="left:494px"></div>
<div class="abs social" style="left:547px"></div>
<div class="abs social" style="left:599px"></div>
<div class="abs social" style="left:652px"></div>
</body>
</html>
```